Copper Ridge Resort & Marina - Boat Slips, Cabin Rentals, Floating Vacation Homes, & More

We need an 8'H x 16'W billboard for our Resort & marina, www.copperridgeresort.example. We'd like it to include: Lakefront Cabin Rentals, Floating Vacation Homes, and New Slips Summer 2022. We'd like it to be simple using the colors on our logo, similar to our business cards, and have our logo on it large. Maybe an arrow on the bottom pointing left that says 3 miles, possibly our website and phone number.

Target Market(s)

Lake People, Boaters

Industry/Entity Type

Resort & Marina (Recreation/Hospitality)

Font styles to use
Sans Serif
Other font styles liked:
• Simple/modern

Colors
0054AA
0677BA
7BADD7
CADEEF
E8F1F8
FFC000
F8CF3A
FAE287
FDF2CF
FEFAEE
F0912C
F2A743
F7CA91
FBE8D2
FDF5EE

Requirements
Must have
• Logo, Cabin Rentals, Floating Vacation Homes, New Slips Summer 2022
Nice to have
• An additional banner hanging from the bottom with an orange (or blue, colors from our logo) arrow pointing left, with white text saying: 3 miles 555-214-0867 www.copperridgeresort.example
Should not have
• Shouldn't be too busy

```html
<!DOCTYPE html>
<html lang="en">
<head>
<meta charset="utf-8">
<title>Copper Ridge Resort &amp; Marina — Billboard</title>
<link href="https://fonts.googleapis.com/css2?family=Libre+Baskerville:wght@400;700&family=Montserrat:wght@600;700&display=swap" rel="stylesheet">
<style>
  :root {
    --page: #f1f1f1;
    --navy: #0e3b70;
    --navy-light: #174a84;
    --navy-mid: #12427a;
    --orange: #f9a825;
    --white: #ffffff;
    --map-fill: #e8f1f8;
    --icon-fill: #cadeef;
  }
  * { margin: 0; padding: 0; box-sizing: border-box; }
  html, body { width: 938px; height: 1200px; overflow: hidden; background: var(--page); }
  .billboard {
    position: absolute; left: 39px; top: 385px; width: 860px; height: 430px;
    background: var(--navy); overflow: hidden;
    box-shadow: 0 4px 14px rgba(0,0,0,.25);
  }
  .facets { position: absolute; inset: 0; }
  .brand {
    position: absolute; left: 40px; top: 122px; width: 470px;
    display: flex; flex-direction: column; align-items: center;
  }
  .brand-name {
    font-family: "Libre Baskerville", serif; font-weight: 400;
    font-size: 46px; line-height: 1; letter-spacing: 1px;
    color: var(--white); white-space: nowrap;
  }
  .brand-tag {
    font-family: "Montserrat", sans-serif; font-weight: 600;
    font-size: 19px; letter-spacing: 9px; margin-top: 12px;
    color: var(--orange); white-space: nowrap;
  }
  .lake-map {
    position: absolute; left: 544px; top: 25px; width: 258px; height: 215px;
    background: radial-gradient(ellipse at 60% 50%, var(--map-fill), rgba(232,241,248,.15) 70%);
    border-radius: 40% 50% 45% 55%;
    opacity: .85;
  }
  .lake-label {
    position: absolute; left: 700px; top: 232px;
    font-family: "Libre Baskerville", serif; font-weight: 700; font-size: 15px; color: var(--white);
  }
  .feature { position: absolute; top: 266px; height: 56px; display: flex; align-items: center; }
  .feature-icon { width: 50px; height: 50px; background: var(--icon-fill); opacity: .35; border-radius: 4px; }
  .feature-rule { width: 2px; height: 56px; background: var(--orange); margin: 0 10px 0 11px; }
  .feature-text {
    font-family: "Libre Baskerville", serif; font-weight: 700; font-size: 23px; line-height: 29px;
    color: var(--orange); white-space: nowrap;
  }
  .feature--cabins { left: 50px; }
  .feature--floating { left: 258px; }
  .feature--slips { left: 570px; }
  .info-bar {
    position: absolute; top: 361px; height: 30px;
    background: var(--orange); color: var(--white);
    font-family: "Montserrat", sans-serif; font-weight: 700; font-size: 17px;
    display: flex; align-items: center; justify-content: center; gap: 9px;
  }
  .directions { position: absolute; left: 50px; top: 347px; width: 184px; height: 58px; }
  .directions-label {
    position: absolute; left: 39px; top: 14px; width: 145px; height: 30px;
    display: flex; align-items: center; justify-content: center;
    font-family: "Montserrat", sans-serif; font-weight: 700; font-size: 17px; color: var(--white);
  }
  .info-bar--web { left: 246px; width: 358px; }
  .info-bar--phone { left: 618px; width: 191px; }
</style>
</head>
<body>
  <main class="billboard">
    <svg class="facets" width="860" height="430" viewBox="0 0 860 430" aria-hidden="true">
      <polygon points="125,0 480,0 550,190 150,430 20,430 0,400 0,260" fill="var(--navy-light)"/>
      <polygon points="480,0 650,0 520,260 430,430 150,430 550,190" fill="var(--navy-mid)"/>
      <polygon points="520,260 860,60 860,430 430,430" fill="var(--navy-mid)" opacity=".6"/>
    </svg>

    <div class="brand">
      <div class="brand-name">COPPER RIDGE</div>
      <div class="brand-tag">resort &amp; marina</div>
    </div>

    <div class="lake-map" role="img" aria-label="White silhouette map of Lake Texoma with a star marking the resort location"></div>
    <div class="lake-label">Lake Texoma</div>

    <div class="feature feature--cabins">
      <div class="feature-icon" role="img" aria-label="Line icon of a log cabin"></div>
      <div class="feature-rule"></div>
      <div class="feature-text">Cabin<br>Rentals</div>
    </div>
    <div class="feature feature--floating">
      <div class="feature-icon" role="img" aria-label="Line icon of a house floating on water"></div>
      <div class="feature-rule"></div>
      <div class="feature-text">Floating<br>Vacation Homes</div>
    </div>
    <div class="feature feature--slips">
      <div class="feature-icon" role="img" aria-label="Line icon of a boat dock with trees"></div>
      <div class="feature-rule"></div>
      <div class="feature-text">New Slips<br>Summer 2022</div>
    </div>

    <div class="directions">
      <svg width="184" height="58" viewBox="0 0 184 58" aria-hidden="true">
        <polygon points="0,29 39,0 39,14 184,14 184,44 39,44 39,58" fill="var(--orange)"/>
      </svg>
      <div class="directions-label">3 MILES</div>
    </div>

    <div class="info-bar info-bar--web">
      <svg width="15" height="15" viewBox="0 0 24 24" aria-hidden="true">
        <circle cx="12" cy="12" r="9" fill="none" stroke="var(--white)" stroke-width="2"/>
        <path d="M3 12h18M12 3c3 3 3 15 0 18M12 3c-3 3-3 15 0 18" fill="none" stroke="var(--white)" stroke-width="1.6"/>
      </svg>
      www.copperridgeresort.example
    </div>
    <div class="info-bar info-bar--phone">
      <svg width="15" height="15" viewBox="0 0 24 24" aria-hidden="true">
        <path d="M6.6 10.8a15.1 15.1 0 0 0 6.6 6.6l2.2-2.2a1 1 0 0 1 1-.25 11.4 11.4 0 0 0 3.6.57 1 1 0 0 1 1 1V20a1 1 0 0 1-1 1A17 17 0 0 1 3 4a1 1 0 0 1 1-1h3.5a1 1 0 0 1 1 1c0 1.25.2 2.45.57 3.57a1 1 0 0 1-.25 1z" fill="none" stroke="var(--white)" stroke-width="2"/>
      </svg>
      555-214-0867
    </div>
  </main>
</body>
</html>
```